Redesign of my business card

I would like to redesign my business card attached is my old version the new one. I’d like using my new logo that you designed that looks amazing thank you.

I would like the new card to be minimalist Tundra Property Group’s two key activities. I would also like on the card commercial cleaning at Facilities maintenance.

```html
<!DOCTYPE html>
<html lang="en">
<head>
<meta charset="utf-8">
<title>Tundra Property Group – Business Card</title>
<link href="https://fonts.googleapis.com/css2?family=Arimo:wght@400;700&display=swap" rel="stylesheet">
<style>
  :root {
    --stage: #3d3d3d;
    --card-white: #ffffff;
    --brand-blue: #1170bb;
    --brand-blue-deep: #0d5aa0;
    --ink-dark: #2b2b2b;
    --ink-grey: #6b6b6b;
    --rule-grey: #c9c9c9;
    --block-dark: #2f2f2f;
  }
  * { box-sizing: border-box; margin: 0; padding: 0; }
  html, body {
    width: 1200px; height: 803px; overflow: hidden;
    background: var(--stage);
    font-family: "Arimo", Arial, sans-serif;
  }
  .stage {
    position: relative; width: 1200px; height: 803px;
    display: flex; align-items: center; justify-content: center; gap: 60px;
  }
  .card {
    position: relative; width: 510px; height: 292px;
    border-radius: 22px; overflow: hidden;
  }

  /* Front card */
  .card--front { background: var(--card-white); }
  .front__brand {
    position: absolute; left: 40px; top: 112px;
    font-size: 25px; font-weight: 700; color: var(--brand-blue-deep);
    line-height: 1.1; width: 170px;
  }
  .front__divider {
    position: absolute; left: 228px; top: 86px; width: 1px; height: 110px;
    background: var(--rule-grey);
  }
  .front__person { position: absolute; left: 252px; top: 86px; }
  .front__name { font-size: 24px; font-weight: 700; color: var(--brand-blue-deep); }
  .front__title { font-size: 13px; color: var(--ink-grey); margin-top: 2px; }
  .front__contacts { list-style: none; margin-top: 20px; }
  .front__contacts li {
    display: flex; align-items: center; gap: 8px;
    font-size: 13.5px; color: var(--ink-dark); margin-bottom: 5px;
  }
  .front__contacts svg { width: 12px; height: 12px; flex: none; }
  .front__band {
    position: absolute; left: 0; top: 224px; width: 446px; height: 34px;
    background: var(--brand-blue);
    display: flex; align-items: center; justify-content: center;
    color: var(--card-white); font-size: 14px; letter-spacing: 3px;
  }
  .front__marker {
    position: absolute; left: 456px; top: 229px; width: 24px; height: 24px;
    background: var(--brand-blue);
  }
  .front__block {
    position: absolute; right: 0; top: 172px; width: 28px; height: 52px;
    background: var(--block-dark);
  }

  /* Back card */
  .card--back {
    background: var(--brand-blue);
    display: flex; flex-direction: column; align-items: center; justify-content: center;
  }
  .back__brand {
    font-size: 40px; font-weight: 700; color: var(--card-white);
    margin-top: -10px;
  }
  .back__services {
    margin-top: 58px; font-size: 15px; color: var(--card-white);
    display: flex; gap: 12px;
  }
</style>
</head>
<body>
<main class="stage">
  <section class="card card--front" aria-label="Business card front">
    <div class="front__brand">Tundra Property Group</div>
    <div class="front__divider"></div>
    <div class="front__person">
      <h1 class="front__name">Liam Carter</h1>
      <p class="front__title">President</p>
      <ul class="front__contacts">
        <li>
          <svg viewBox="0 0 24 24" aria-hidden="true"><path fill="#1170bb" d="M6.6 10.8a15 15 0 0 0 6.6 6.6l2.2-2.2c.3-.3.7-.4 1-.2 1.1.4 2.3.6 3.6.6.6 0 1 .4 1 1V20c0 .6-.4 1-1 1A17 17 0 0 1 3 4c0-.6.4-1 1-1h3.5c.6 0 1 .4 1 1 0 1.3.2 2.5.6 3.6.1.3 0 .7-.2 1z"/></svg>
          0400 555 019
        </li>
        <li>
          <svg viewBox="0 0 24 24" aria-hidden="true"><rect x="2" y="5" width="20" height="14" rx="1" fill="#1170bb"/><path d="M3 6l9 7 9-7" stroke="#fff" stroke-width="2" fill="none"/></svg>
          info@tundraproperty.com.au
        </li>
      </ul>
    </div>
    <div class="front__band">www.tundraproperty.com.au</div>
    <div class="front__marker"></div>
    <div class="front__block"></div>
  </section>

  <section class="card card--back" aria-label="Business card back">
    <div class="back__brand">Tundra Property Group</div>
    <p class="back__services"><span>Commercial Cleaning</span><span>|</span><span>Facilities Maintenance</span></p>
  </section>
</main>
</body>
</html>
```